Global investment holding company - Business Card Design

Brenvik Holdings is a recently incorporated investment holding company. Based in Singapore, it has operations in global emerging markets in the transport & logistics, energy and livestock industries.

Its tagline "Growth Through Alliance" reflects the company's philosophy of helping countries progress through partnerships which generate employment and share benefits with its society.

We are looking for a business card that reflects our global presence - incorporating the logo design into the business card design. It must have a sophisticated, modern & corporate feel.

Target Market(s)

Investors and high level governmental officials

Industry/Entity Type

Investment

Requirements
Must have
• - Use of shades of blue in logo

-Profile picture

- Name: Dennis Okoro
- Title: Chairman
- Email: dennis@brenvikholdings.example
- Mob: +65 9154 6081
- Tel: +65 6419 5820
- DID: + 65 6419 5821
- Address: 47 Marlow Road, #05-03, Singapore 048812

- website: www.brenvikholdings.example

```html
<!DOCTYPE html>
<html lang="en">
<head>
<meta charset="utf-8">
<title>Brenvik Holdings – Business Card</title>
<link rel="stylesheet" href="https://fonts.googleapis.com/css2?family=Source+Sans+3:wght@400;600;700&display=swap">
<style>
  :root {
    --canvas: #e9ebee;
    --card-white: #ffffff;
    --navy: #1d4f91;
    --blue-deep: #1467b3;
    --blue-mid: #1f86cf;
    --blue-light: #4db3e8;
    --grey-text: #6b6b6b;
    --ink: #2f2f2f;
    --rule-grey: #b9bcc0;
    --photo-top: #c9ccd1;
    --photo-bottom: #3b4656;
  }
  * { box-sizing: border-box; margin: 0; padding: 0; }
  html, body {
    width: 1200px; height: 1108px; overflow: hidden;
    background: var(--canvas);
    font-family: "Source Sans 3", "Myriad Pro", sans-serif;
  }
  .card {
    position: absolute;
    width: 731px; height: 417px;
    overflow: hidden;
    box-shadow: 0 2px 8px rgba(0,0,0,.18);
  }

  /* Front */
  .card-front { left: 94px; top: 94px; background: var(--card-white); }
  .brand { position: absolute; left: 37px; top: 37px; display: flex; align-items: center; gap: 26px; }
  .brand-dot { width: 104px; height: 104px; border-radius: 50%; background: var(--blue-mid); }
  .brand-name { color: var(--navy); font-weight: 700; font-size: 42px; line-height: 42px; letter-spacing: .5px; }
  .tagline-front {
    position: absolute; left: 47px; top: 158px;
    color: var(--grey-text); font-size: 18px; letter-spacing: 1.6px;
  }
  .contact { position: absolute; left: 42px; top: 192px; list-style: none; color: var(--ink); font-size: 17px; line-height: 24px; }
  .contact li { display: flex; align-items: center; gap: 6px; }
  .contact svg { width: 13px; height: 13px; fill: #555; flex: none; }
  .address { position: absolute; left: 38px; top: 296px; color: var(--ink); font-size: 17px; }
  .portrait {
    position: absolute; left: 452px; top: 62px; width: 260px; height: 272px;
    border-radius: 130px 130px 0 0;
    background: linear-gradient(180deg, var(--photo-top) 0%, #8a8f98 55%, var(--photo-bottom) 100%);
  }
  .base-rule { position: absolute; left: 0; right: 0; top: 334px; height: 5px; background: var(--rule-grey); }
  .name-band {
    position: absolute; left: 0; right: 0; top: 345px; bottom: 0;
    background: linear-gradient(90deg, var(--blue-light), var(--blue-mid) 50%, var(--blue-deep));
  }
  .name-line {
    position: absolute; right: 30px; top: 362px; color: #fff; font-size: 19px; line-height: 34px;
  }
  .name-line strong { font-size: 26px; font-weight: 700; }

  /* Back */
  .card-back {
    left: 361px; top: 590px;
    background: radial-gradient(ellipse at 50% 40%, var(--blue-light) 0%, var(--blue-mid) 55%, var(--blue-deep) 100%);
    color: #fff; text-align: center;
  }
  .back-brand { position: absolute; left: 184px; top: 110px; display: flex; align-items: center; gap: 28px; }
  .back-dot { width: 124px; height: 124px; border-radius: 50%; background: #fff; }
  .back-name { font-weight: 700; font-size: 50px; line-height: 52px; text-align: left; }
  .tagline-back { position: absolute; left: 0; right: 0; top: 258px; font-size: 20px; letter-spacing: 2px; }
  .web-back { position: absolute; left: 0; right: 0; top: 346px; font-size: 19px; letter-spacing: 3.5px; }
</style>
</head>
<body>

<section class="card card-front">
  <div class="brand">
    <span class="brand-dot"></span>
    <div class="brand-name">BRENVIK<br>HOLDINGS</div>
  </div>
  <p class="tagline-front">GROWTH THROUGH ALLIANCE</p>

  <ul class="contact">
    <li><svg viewBox="0 0 16 16"><path d="M3 1l3 3-2 2c1 2 3 4 5 5l2-2 3 3-2 3C6 14 2 10 1 3z"/></svg>+65 6419 5820</li>
    <li><svg viewBox="0 0 16 16"><path d="M3 1l3 3-2 2c1 2 3 4 5 5l2-2 3 3-2 3C6 14 2 10 1 3z"/></svg>+ 65 6419 5821(DID)&nbsp;
      <svg viewBox="0 0 16 16"><rect x="4" y="0" width="8" height="16" rx="1.5"/></svg>+65 9154 6081</li>
    <li><svg viewBox="0 0 16 16"><path d="M1 3h14v10H1z"/></svg>dennis@brenvikholdings.example</li>
    <li><svg viewBox="0 0 16 16"><circle cx="8" cy="8" r="7"/></svg>www.brenvikholdings.example</li>
  </ul>
  <p class="address">47 Marlow Road, #05-03, Singapore 048812</p>

  <div class="portrait" role="img" aria-label="Portrait photograph of the chairman"></div>

  <div class="base-rule"></div>
  <div class="name-band"></div>
  <p class="name-line"><strong>Dennis Okoro ,</strong> Chairman</p>
</section>

<section class="card card-back">
  <div class="back-brand">
    <span class="back-dot"></span>
    <div class="back-name">BRENVIK<br>HOLDINGS</div>
  </div>
  <p class="tagline-back">GROWTH THROUGH ALLIANCE</p>
  <p class="web-back">www.brenvikholdings.example</p>
</section>

</body>
</html>
```